Interfaith Forum and Festival Postcard style Flyer

Create a Post Card Design: 6x9

Unity Teen Assembly of Harbor Valley's Annual Spirit Summit and Fair: Teens expressing their Faith Through Art, Music, & Dialogue.
Westmere Institute 27415 Larkfield Suite 240 Brookmere, CA 90871
11:30am-9:00pm
UTAHV.org
like us on Sampleface https://www.sampleface.net/UTAHV/
Contact Person: Rohanpreet Sandhu UTAHVorg@mailbox.example

Task:
We are hosting our 12th annual Crossroads Teen Summit in Orange County. It is also the 3rd annual Spirit Fair.
We are looking for a large postcard like flyer front and back that will highlight our event that we can send out
Please include our UTAHV logo as well as our Bright Harbor Allies logo
Please feel free to clean up/crop pics if necessary

Additional Info to include:
• RSVP for our SPIRIT SUMMIT by February 1st, 2016
• To Participate in our Spirit Fair (Music, Song, Dance) RSVP by February 12th, 2016
• Art work Must be Submitted by: March 1st, 2015

(High School Students only)

Useful Background info (not necessary to include):

http://utahv.org/about/

Crossroads Teen Summit
This year's theme "Shared Horizons"
All high school age faith groups are invited to come and join with 100 to 150 other high school students from various faith traditions to participate in the Unity Teen Assembly of Harbor Valley‘s Annual Crossroads Teen Summit.
The purpose of this Crossroads Teen Summit is to bring together young people from diverse ethnic, cultural, and religious backgrounds, and to engage them in dialogue. True dialogue is a conversation on a common subject between two or more persons of differing points of view and/or backgrounds. This dialogue’s purpose is two-fold: first, for each participant to learn from the other so that he or she can understand and grow; second, for each participating adult to learn from the young what they think, what their concerns are, and how they deal with differing points of view. We feel that this commitment to dialogue will affect relationships in a constructive way in our places of worship and in our community.
The forum itself involves having eight high school-age kids and one adult youth leader around each table to discuss a common question.
Our intent is to make each discussion group as religiously diverse as possible. Our youth leaders act as facilitators, but it is stressed that it is the students we want to hear from. The facilitator is there only to encourage the dialogue.
The forum will be followed by the Spirit Fair where families of the participants are welcomed to join. This event will include and Art gallery display of the teens, highlighting their expressions of faith

Target Market(s)

Youth and Interfaith Organizations and Places of Worship

Industry/Entity Type

Festival

Colors
f37022
faa54b
f78f20

Requirements
Must have
• Both Logos
• Unity Teen Assembly of Harbor Valley's Annual Spirit Summit and Fair: Teens expressing their Faith Through Art, Music, & Dialogue.
• Westmere Institute 27415 Larkfield Suite 240 Brookmere, CA 90871
• 11:30am-9:00pm
• UTAHV.org
• like us on Sampleface https://www.sampleface.net/UTAHV/
• Contact Person: Rohanpreet Sandhu UTAHVorg@mailbox.example
• RSVP Info (please look at Project description)
Should not have
• does not need to include all the background info

```html
<!DOCTYPE html>
<html lang="en">
<head>
<meta charset="utf-8">
<title>Spirit Summit and Fair Postcard</title>
<link rel="stylesheet" href="https://fonts.googleapis.com/css2?family=Titan+One&family=Didact+Gothic&family=Josefin+Sans:wght@300;400;600&display=swap">
<style>
  :root {
    --orange: #f37022;
    --orange-light: #faa54b;
    --orange-mid: #f78f20;
    --orange-deep: #ee5a24;
    --orange-pale: #f6c08c;
    --beige: #e7e2d4;
    --brown: #3a2a22;
    --navy: #2d3f6b;
    --magenta: #e2157a;
    --green: #6cbf2c;
    --purple: #7a2f8f;
    --white: #ffffff;
    --ink: #333333;
  }
  * { margin: 0; padding: 0; box-sizing: border-box; }
  html, body { width: 1200px; height: 848px; overflow: hidden; background: var(--white); }
  .canvas { position: relative; width: 1200px; height: 848px; font-family: "Didact Gothic", sans-serif; }

  /* Front */
  .card-front {
    position: absolute; left: 48px; top: 86px; width: 436px; height: 654px; overflow: hidden;
    background: radial-gradient(circle at 50% 45%, var(--orange-pale), var(--orange-light) 45%, var(--orange-mid) 75%, var(--orange) 100%);
  }
  .front-panel {
    position: absolute; left: 16px; top: 24px; width: 404px; height: 612px;
    background: var(--beige);
    border: 5px dotted var(--brown);
  }
  .partner-logos { position: absolute; left: 122px; top: 34px; display: flex; align-items: center; gap: 14px; }
  .logo-name { font-family: "Josefin Sans", sans-serif; font-weight: 600; font-size: 13px; color: var(--navy); display: flex; align-items: center; gap: 5px; line-height: 1; }
  .logo-mark { width: 16px; height: 16px; border-radius: 50%; border: 1.5px solid var(--navy); }

  .ribbon { position: absolute; left: 52px; top: 80px; width: 300px; height: 42px; }
  .ribbon svg { position: absolute; left: -30px; top: 0; }
  .ribbon-text {
    position: absolute; left: 0; top: 3px; width: 300px; text-align: center;
    font-family: "Josefin Sans", sans-serif; font-size: 12.5px; line-height: 15px; color: var(--white);
  }
  .headline { position: absolute; left: 0; top: 133px; width: 394px; text-align: center; font-family: "Titan One", sans-serif; font-weight: 400; font-size: 22px; line-height: 27px; color: var(--orange-deep); }
  .headline .art { color: var(--magenta); }
  .headline .music { color: var(--green); }
  .headline .and { color: var(--orange); }
  .headline .dialogue { color: var(--purple); }

  .venue { position: absolute; left: 0; top: 227px; width: 394px; text-align: center; font-size: 13px; color: var(--brown); }
  .hours { position: absolute; left: 0; top: 247px; width: 394px; text-align: center; font-family: "Titan One", sans-serif; font-size: 24px; color: var(--brown); }
  .contact { position: absolute; left: 0; top: 281px; width: 394px; text-align: center; font-size: 11.5px; line-height: 14px; color: var(--brown); }
  .contact svg { vertical-align: -2px; }

  .photo { position: absolute; border: 3px solid var(--white); box-shadow: 1px 2px 4px rgba(0,0,0,.35); }
  .photo-craft { left: 26px; top: 308px; width: 75px; height: 48px; background: linear-gradient(135deg, #c9a3a8, #8c5e5a); transform: rotate(-6deg); }
  .photo-group { left: -11px; top: 330px; width: 272px; height: 155px; background: linear-gradient(160deg, #8a9a6a, #4d4a3c 60%, #2b2824); transform: rotate(-1.5deg); }
  .photo-table { left: 126px; top: 440px; width: 127px; height: 85px; background: linear-gradient(135deg, #b09a82, #6e5a48); transform: rotate(2deg); }
  .photo-sky { left: 22px; top: 465px; width: 102px; height: 80px; background: linear-gradient(180deg, #b9c3cc, #c89a76); transform: rotate(-3deg); }
  .photo-dance { left: 257px; top: 460px; width: 104px; height: 85px; background: linear-gradient(180deg, #d8d4cc, #8a7a6a); transform: rotate(4deg); }
  .photo-teens { left: 91px; top: 520px; width: 130px; height: 82px; background: linear-gradient(135deg, #a08468, #4e3c2e); transform: rotate(-2deg); }
  .photo-stage { left: 221px; top: 525px; width: 78px; height: 60px; background: linear-gradient(135deg, #7a6c64, #3c3430); transform: rotate(5deg); }

  /* Back */
  .card-back { position: absolute; left: 500px; top: 185px; width: 655px; height: 435px; background: var(--beige); }
  .back-message { position: absolute; left: 0; top: 0; width: 326px; height: 435px; background: var(--orange-mid); color: var(--white); text-align: center; }
  .back-kicker { position: absolute; top: 25px; width: 100%; font-family: "Josefin Sans", sans-serif; font-size: 8.5px; }
  .back-headline { position: absolute; top: 36px; width: 100%; font-family: "Titan One", sans-serif; font-weight: 400; font-size: 12.5px; line-height: 15px; }
  .back-title { position: absolute; top: 77px; width: 100%; font-family: "Josefin Sans", sans-serif; font-weight: 300; font-size: 13px; line-height: 16px; color: var(--brown); }
  .back-body { position: absolute; top: 114px; left: 16px; width: 294px; font-size: 6.7px; line-height: 9.6px; color: var(--brown); }
  .back-body p { margin-bottom: 9px; }
  .rsvp { position: absolute; left: 0; bottom: 0; width: 326px; height: 87px; background: var(--orange-deep); padding: 6px 10px; }
  .rsvp-inner { border: 1px dashed var(--white); height: 100%; padding-top: 6px; font-size: 10px; line-height: 12px; color: var(--white); }
  .stamp-box { position: absolute; left: 568px; top: 25px; width: 60px; height: 88px; border: 1px solid var(--ink); }
  .address-line { position: absolute; height: 1px; background: var(--ink); }
</style>
</head>
<body>
<div class="canvas">

  <section class="card-front">
    <div class="front-panel">
      <div class="partner-logos">
        <span class="logo-name"><span class="logo-mark"></span>Bright Harbor Allies</span>
        <span class="logo-name"><span class="logo-mark"></span>UTAHV</span>
      </div>

      <div class="ribbon">
        <svg width="360" height="42" viewBox="0 0 360 42" aria-hidden="true">
          <polygon points="0,10 34,10 34,40 0,40 12,25" fill="#d85a1c"/>
          <polygon points="360,10 326,10 326,40 360,40 348,25" fill="#d85a1c"/>
          <rect x="30" y="0" width="300" height="36" fill="#f78f20"/>
        </svg>
        <p class="ribbon-text">Unity Teen Assembly of Harbor Valley's<br>12th Annual Spirit Summit and Fair</p>
      </div>

      <h1 class="headline">TEENS EXPRESSING<br>THEIR FAITH THROUGH<br><span class="art">ART,</span> <span class="music">MUSIC,</span> <span class="and">AND</span> <span class="dialogue">DIALOGUE.</span></h1>

      <p class="venue">Westmere Institute 27415 Larkfield Suite 240 Brookmere, CA 90871</p>
      <p class="hours">11:30AM-9:00PM</p>
      <p class="contact">
        www.UTAHV.org | Sampleface UTAHV<br>
        Rohanpreet Sandhu:
        <svg width="12" height="9" viewBox="0 0 12 9" aria-hidden="true"><rect x="0.5" y="0.5" width="11" height="8" fill="none" stroke="#3a2a22"/><polyline points="0.5,0.5 6,5 11.5,0.5" fill="none" stroke="#3a2a22"/></svg>
        UTAHVorg@mailbox.example
      </p>

      <div class="photo photo-craft" role="img" aria-label="Photo of student craft table"></div>
      <div class="photo photo-group" role="img" aria-label="Group photo of forum participants outdoors"></div>
      <div class="photo photo-table" role="img" aria-label="Photo of a discussion table"></div>
      <div class="photo photo-sky" role="img" aria-label="Student painting of a sunset sky"></div>
      <div class="photo photo-dance" role="img" aria-label="Photo of a dance performance"></div>
      <div class="photo photo-teens" role="img" aria-label="Photo of teens standing together"></div>
      <div class="photo photo-stage" role="img" aria-label="Photo of a stage performance"></div>
    </div>
  </section>

  <section class="card-back">
    <div class="back-message">
      <p class="back-kicker">Unity Teen Assembly of Harbor Valley's 12th Annual Spirit Summit and Fair</p>
      <h2 class="back-headline">TEENS EXPRESSING THEIR FAITH THROUGH<br>ART, MUSIC, AND DIALOGUE.</h2>
      <h3 class="back-title">CROSSROADS TEEN SUMMIT<br>This year's theme "Shared Horizons"</h3>
      <div class="back-body">
        <p>All high school age faith groups are invited to come and join with 100 to 150 other high school students from various faith traditions to participate in the Unity Teen Assembly of Harbor Valley's Annual Crossroads Teen Summit.</p>
        <p>The purpose of this Crossroads Teen Summit is to bring together young people from diverse ethnic, cultural, and religious backgrounds, and to engage them in dialogue. True dialogue is a conversation on a common subject between two or more persons of differing points of view and/or backgrounds. This dialogue's purpose is two-fold: first, for each participant to learn from the other so that he or she can understand and grow; second, for each participating adult to learn from the young what they think, what their concerns are, and how they deal with differing points of view. We feel that this commitment to dialogue will affect relationships in a constructive way in our places of worship and in our community.</p>
        <p>The forum itself involves having eight high school-age kids and one adult youth leader around each table to discuss a common question.<br>Our intent is to make each discussion group as religiously diverse as possible. Our youth leaders act as facilitators, but it is stressed that it is the students we want to hear from. The facilitator is there only to encourage the dialogue.</p>
        <p>The forum will be followed by the Spirit Fair where families of the participants are welcomed to join. This event will include and Art gallery display of the teens, highlighting their expressions of faith</p>
      </div>
      <div class="rsvp">
        <div class="rsvp-inner">
          RSVP for our SPIRIT SUMMIT by February 1st, 2016<br>
          To Participate in our Spirit Fair (Music, Song, Dance)<br>
          RSVP by February 12th, 2016<br>
          Art work Must be Submitted by: March 1st, 2015<br>
          (High School Students only)
        </div>
      </div>
    </div>
    <div class="stamp-box"></div>
    <div class="address-line" style="left:368px; top:211px; width:260px;"></div>
    <div class="address-line" style="left:368px; top:253px; width:260px;"></div>
    <div class="address-line" style="left:368px; top:293px; width:260px;"></div>
    <div class="address-line" style="left:490px; top:342px; width:138px;"></div>
  </section>

</div>
</body>
</html>
```